R. P. Pelsar & Associates, Inc

Rodrigo Pelsar
Accountant
4213 SE 87th AVE
Larkfield, Nevada 89907
(555) 482-0917
rod.pelsar@quillmail.net
Accounting - Tax Preparation Services - Bookkeeping
Side - one business logo on the left and business information on right
On Backside: The logo in the middle and under the logo my company name.

Rounded Corner of the cards
In reference to the logo and cards I need to adjust the circle around the RP and color.

```html
<!DOCTYPE html>
<html lang="en">
<head>
<meta charset="UTF-8">
<title>R. P. Pelsar &amp; Associates, Inc – Business Cards</title>
<link rel="stylesheet" href="https://fonts.googleapis.com/css2?family=Poppins:wght@400;500;600;700&display=swap">
<style>
  :root {
    --brand-blue: #1872c2;
    --brand-blue-soft: #2a7fcb;
    --ink: #1c1c1e;
    --paper: #ffffff;
    --stage: #e9eaec;
    --muted: #2b2b2b;
  }
  * { box-sizing: border-box; margin: 0; padding: 0; }
  html, body {
    width: 1200px; height: 800px; overflow: hidden;
    background: var(--stage);
    font-family: "Poppins", sans-serif;
  }
  .stage {
    width: 1200px; height: 800px;
    display: flex; align-items: center; justify-content: center; gap: 40px;
  }
  .card {
    width: 560px; height: 320px;
    border-radius: 26px;
    position: relative; overflow: hidden;
    box-shadow: 0 10px 30px rgba(0,0,0,.18);
  }

  /* Back side */
  .card--back {
    background: var(--brand-blue);
    color: var(--paper);
    display: flex; flex-direction: column; align-items: center; justify-content: center;
  }
  .monogram-pattern {
    position: absolute; inset: 0;
    background: linear-gradient(135deg, var(--brand-blue-soft), var(--brand-blue));
  }
  .back-content { position: relative; text-align: center; }
  .brand-mark {
    display: flex; align-items: center; justify-content: center; gap: 10px;
    font-weight: 600; font-size: 30px; letter-spacing: .5px;
  }
  .brand-mark__dot {
    width: 18px; height: 18px; border-radius: 50%;
    border: 3px solid currentColor;
  }
  .company-name {
    margin-top: 22px; line-height: 1.15;
  }
  .company-name__main { font-weight: 700; font-size: 22px; letter-spacing: 1px; }
  .company-name__sub { font-weight: 400; font-size: 17px; letter-spacing: 1px; }

  /* Front side */
  .card--front { background: var(--paper); color: var(--ink); }
  .front-body {
    position: absolute; left: 0; right: 0; top: 0; height: 252px;
    display: flex; align-items: center;
  }
  .front-logo {
    width: 230px; display: flex; justify-content: center;
  }
  .front-logo .brand-mark { color: var(--ink); font-size: 24px; }
  .divider {
    width: 1px; height: 130px; background: var(--brand-blue);
  }
  .contact {
    padding-left: 30px; font-size: 12.5px; line-height: 1.45;
  }
  .contact__name { font-weight: 600; font-size: 21px; line-height: 1.1; }
  .contact__role { color: var(--brand-blue); font-weight: 500; font-size: 14px; margin-bottom: 14px; }
  .contact__address { margin-bottom: 12px; color: var(--muted); }
  .contact__line { display: flex; align-items: center; gap: 8px; color: var(--muted); }
  .contact__icon {
    width: 17px; height: 17px; border-radius: 50%;
    background: var(--brand-blue);
    display: flex; align-items: center; justify-content: center; flex: none;
  }
  .services-band {
    position: absolute; left: 0; right: 0; top: 252px; height: 40px;
    background: var(--brand-blue);
    color: var(--paper);
    display: flex; align-items: center; justify-content: center;
    font-size: 14.5px; font-weight: 500; letter-spacing: .4px;
    border-bottom: 3px solid var(--ink);
  }
</style>
</head>
<body>
<main class="stage">
  <section class="card card--back" aria-label="Card back">
    <div class="monogram-pattern" role="img" aria-label="Faint repeated monogram pattern on blue"></div>
    <div class="back-content">
      <div class="brand-mark"><span class="brand-mark__dot"></span><span>R. P. Pelsar</span></div>
      <div class="company-name">
        <div class="company-name__main">R. P. PELSAR &amp;</div>
        <div class="company-name__sub">ASSOCIATES, INC</div>
      </div>
    </div>
  </section>

  <section class="card card--front" aria-label="Card front">
    <div class="front-body">
      <div class="front-logo">
        <div class="brand-mark"><span class="brand-mark__dot"></span><span>R. P. Pelsar</span></div>
      </div>
      <div class="divider"></div>
      <div class="contact">
        <div class="contact__name">Rodrigo Pelsar</div>
        <div class="contact__role">Accountant</div>
        <div class="contact__address">4213 SE 87th AVE<br>Larkfield, Nevada 89907</div>
        <div class="contact__line">
          <span class="contact__icon">
            <svg width="10" height="10" viewBox="0 0 24 24"><path fill="#fff" d="M6.6 10.8a15.1 15.1 0 0 0 6.6 6.6l2.2-2.2c.3-.3.7-.4 1-.2 1.1.4 2.3.6 3.6.6.6 0 1 .4 1 1V20c0 .6-.4 1-1 1A17 17 0 0 1 3 4c0-.6.4-1 1-1h3.5c.6 0 1 .4 1 1 0 1.3.2 2.5.6 3.6.1.3 0 .7-.2 1z"/></svg>
          </span>
          <span>(555) 482-0917</span>
        </div>
        <div class="contact__line">
          <span class="contact__icon">
            <svg width="10" height="10" viewBox="0 0 24 24"><path fill="#fff" d="M3 5h18c.6 0 1 .4 1 1v12c0 .6-.4 1-1 1H3c-.6 0-1-.4-1-1V6c0-.6.4-1 1-1zm9 7 8-5H4z"/></svg>
          </span>
          <span>rod.pelsar@quillmail.net</span>
        </div>
      </div>
    </div>
    <div class="services-band">Accounting | Tax Preparation Services | Bookkeeping</div>
  </section>
</main>
</body>
</html>
```